Corvant Systems Business Card

Create an appealing and elegant Business card for corvant systems. Include logo and use related colors from website, be creative. Include Business name, my name, tile, address, contacts, address, and social media contacts if possible. Logo PSD file is attached.

Bleed Area: 3.46" x 2.32"
Trim: 3.3" x 2.16"
Safe Area: 3.14" x 2.02"

Save files as vector-based PDF with outlined text and PNG.
No crop marks
CMYK color setting

Business Card Info:

Corvant Systems

Dennis Halvorsen
Owner

512 Brindlemoor Rd Unit C
West Warwick, RI 02871
t. 1.888.555.0162
e. dennis.h@corvantsys.example
w. www.corvantsys.example

facebook. www.facebook.com/CorvantSys
twitter. twitter.com/corvantsys
pinterest. www.pinterest.com/corvantsys/

Target Market(s)

Business Owners and Partners

Industry/Entity Type

Business

Requirements
Must have
• Logo and related colors from website

```html
<!DOCTYPE html>
<html lang="en">
<head>
<meta charset="utf-8">
<title>Corvant Systems Business Card</title>
<link href="https://fonts.googleapis.com/css2?family=Open+Sans:wght@300;400;600;700&display=swap" rel="stylesheet">
<style>
  :root {
    --bg: #e4e4e2;
    --card: #f6f6f4;
    --ink: #1f1f1f;
    --ink-soft: #3c3c3c;
    --muted: #5a5a5a;
    --rule: #9a9a9a;
    --blue-deep: #2c5a8f;
    --blue-mid: #3e74b0;
    --blue-light: #6aa6dc;
    --icon-line: #a9cdf0;
  }
  * { box-sizing: border-box; margin: 0; padding: 0; }
  html, body { width: 1200px; height: 1050px; overflow: hidden; }
  body {
    background: var(--bg);
    font-family: "Open Sans", Arial, sans-serif;
    color: var(--ink);
    position: relative;
  }
  .card {
    position: absolute;
    left: 250px;
    width: 700px;
    height: 458px;
    background: var(--card);
    border-radius: 24px;
    overflow: hidden;
    box-shadow: 0 2px 10px rgba(0,0,0,0.12);
  }
  .card--front { top: 50px; }
  .card--back { top: 542px; }

  /* Front */
  .front-band {
    position: absolute; left: 0; top: 0; bottom: 0; width: 46px;
    background: linear-gradient(180deg, var(--blue-light), var(--blue-mid) 45%, var(--blue-deep));
  }
  .front-brand {
    position: absolute; left: 46px; right: 0; top: 0; bottom: 0;
    display: flex; align-items: center; justify-content: center; gap: 26px;
  }
  .brand-mark {
    width: 64px; height: 64px; border-radius: 50%;
    background: var(--blue-mid);
    flex: none;
  }
  .front-name {
    font-weight: 400; font-size: 62px; line-height: 1.02;
    color: var(--ink); letter-spacing: 0.5px;
  }

  /* Back */
  .back-band {
    position: absolute; right: 0; top: 0; bottom: 0; width: 72px;
    background: linear-gradient(270deg, var(--blue-light), var(--blue-mid) 40%, var(--blue-deep));
    display: flex; flex-direction: column; align-items: center; justify-content: center; gap: 14px;
  }
  .band-icon { width: 34px; height: 34px; display: block; }
  .identity {
    position: absolute; left: 42px; top: 58px; width: 280px;
  }
  .identity-name {
    font-weight: 400; font-size: 36px; line-height: 1.05; color: var(--ink);
  }
  .address {
    margin-top: 34px;
    font-size: 18px; line-height: 1.4; font-weight: 400; color: var(--ink-soft);
  }
  .divider {
    position: absolute; left: 342px; top: 56px; bottom: 56px;
    width: 1px; background: var(--rule);
  }
  .contact {
    position: absolute; left: 368px; top: 58px; width: 250px;
  }
  .person { font-weight: 700; font-size: 24px; line-height: 1.2; color: var(--ink); }
  .role {
    font-weight: 400; font-size: 15px; letter-spacing: 1px; color: var(--blue-mid);
    margin-bottom: 22px;
  }
  .phone { font-weight: 600; font-size: 19px; letter-spacing: 0.5px; color: var(--ink); }
  .email { font-weight: 700; font-size: 13px; color: var(--ink-soft); margin-top: 4px; }
  .web { font-weight: 600; font-size: 15px; color: var(--blue-deep); margin-top: 6px; margin-bottom: 16px; }
  .social { font-size: 13px; line-height: 1.6; color: var(--muted); }
</style>
</head>
<body>

  <section class="card card--front" aria-label="Business card front">
    <div class="front-band"></div>
    <div class="front-brand">
      <span class="brand-mark"></span>
      <div class="front-name">Corvant<br>Systems</div>
    </div>
  </section>

  <section class="card card--back" aria-label="Business card back">
    <div class="identity">
      <div class="identity-name">Corvant<br>Systems</div>
      <p class="address">512 Brindlemoor Rd Unit C<br>West Warwick<br>RI 02871</p>
    </div>

    <div class="divider"></div>

    <div class="contact">
      <p class="person">Dennis Halvorsen</p>
      <p class="role">OWNER</p>
      <p class="phone">1.888.555.0162</p>
      <p class="email">dennis.h@corvantsys.example</p>
      <p class="web">www.corvantsys.example</p>
      <p class="social">www.facebook.com/CorvantSys<br>twitter.com/corvantsys<br>www.pinterest.com/corvantsys/</p>
    </div>

    <div class="back-band">
      <svg class="band-icon" viewBox="0 0 34 34" aria-label="Phone">
        <circle cx="17" cy="17" r="15" fill="none" stroke="var(--icon-line)" stroke-width="1.6"/>
        <path d="M12 10c1-1 2-1 2.6 0l1.4 2.4c.4.7.2 1.4-.4 1.9l-.8.6c.8 1.8 2.1 3.1 3.9 3.9l.6-.8c.5-.6 1.2-.8 1.9-.4l2.4 1.4c1 .6 1 1.6 0 2.6-1.5 1.5-3.5 1.4-6.3-.4-2.2-1.5-3.9-3.2-5.3-5.4-1.7-2.7-1.5-4.4 0-5.8z" fill="none" stroke="var(--icon-line)" stroke-width="1.4"/>
      </svg>
      <svg class="band-icon" viewBox="0 0 34 34" aria-label="Email">
        <circle cx="17" cy="17" r="15" fill="none" stroke="var(--icon-line)" stroke-width="1.6"/>
        <rect x="10" y="12" width="14" height="10" fill="none" stroke="var(--icon-line)" stroke-width="1.4"/>
        <path d="M10 12l7 6 7-6" fill="none" stroke="var(--icon-line)" stroke-width="1.4"/>
      </svg>
      <svg class="band-icon" viewBox="0 0 34 34" aria-label="Website">
        <circle cx="17" cy="17" r="15" fill="none" stroke="var(--icon-line)" stroke-width="1.6"/>
        <rect x="12.5" y="9.5" width="9" height="15" rx="1.5" fill="none" stroke="var(--icon-line)" stroke-width="1.4"/>
        <line x1="15" y1="21.5" x2="19" y2="21.5" stroke="var(--icon-line)" stroke-width="1.4"/>
      </svg>
      <svg class="band-icon" viewBox="0 0 34 34" aria-label="Social profile">
        <circle cx="17" cy="17" r="15" fill="none" stroke="var(--icon-line)" stroke-width="1.6"/>
      </svg>
      <svg class="band-icon" viewBox="0 0 34 34" aria-label="Social profile">
        <circle cx="17" cy="17" r="15" fill="none" stroke="var(--icon-line)" stroke-width="1.6"/>
      </svg>
      <svg class="band-icon" viewBox="0 0 34 34" aria-label="Social profile">
        <circle cx="17" cy="17" r="15" fill="none" stroke="var(--icon-line)" stroke-width="1.6"/>
      </svg>
    </div>
  </section>

</body>
</html>
```